Redesign our iOS App Design mockups

- Redesign our current Veltro App Mockup
- Keep the design simple so that programmers do not have to do too much extra work to make your design work.
- Look at the attached website screenshot for the overall look and feel, and color scheme
- Convert the attached vector logo to iOS Icon format.
- Deliver all graphics in the density required for Veltro QL Prime.
- I have attached the current iOS mockup in a .ZIP file but you can view it here as well: https://boards.mockvault.net/share/QWTRPL8HNB2

Target Market(s)

Mostly Male Internet Consumers between the ages of 20 and 35

Industry/Entity Type

Internet

Colors

Designer to choose colors to be used in the design.

Requirements
Must have
• - Deliver all graphics in the density required for Veltro QL Prime
• - Should also look good on Tabrix and Tabrix pro
• - Design type should be “FLAT.”
• - Spell out fonts used in the design and where they are used. Also, include font sizes.
• - Please use ALL the elements in each page and use all placements and text EXACTLY. Please do not improvise with text or components.
• I have designed the mockup exactly the way I like it. I just want it to made to look better.
Should not have

```html
<!DOCTYPE html>
<html lang="en">
<head>
<meta charset="utf-8">
<title>CozyTunnel – Forgot Password &amp; Home Screen</title>
<link rel="stylesheet" href="https://fonts.googleapis.com/css2?family=Roboto:wght@300;400;500&display=swap">
<style>
:root{
  --canvas:#f4f4f6;
  --screen-bg:#f7f7f9;
  --row-bg:#ffffff;
  --section-bg:#f1f1f4;
  --text:#111114;
  --muted:#b3b3bb;
  --label:#8a93a6;
  --section-label:#5f5f66;
  --divider:#dcdce2;
  --accent:#f25a4f;
  --ios-blue:#1a7cf5;
  --black:#000000;
  --chevron:#b8b8c0;
  --star-on:#f8c51c;
  --star-off:#b9b9bf;
}
*{box-sizing:border-box;margin:0;padding:0}
html,body{width:1200px;height:1200px;overflow:hidden;background:var(--canvas);
  font-family:"Roboto",system-ui,sans-serif;color:var(--text)}
.screen{position:absolute;top:174px;width:372px;height:804px;border-radius:38px;
  overflow:hidden;background:var(--screen-bg);box-shadow:0 24px 60px rgba(0,0,0,.14)}
.screen--forgot{left:210px}
.screen--home{left:706px;background:var(--section-bg)}
.abs{position:absolute}
.status{top:0;left:0;right:0;height:44px;background:var(--row-bg)}
.status__time{position:absolute;left:35px;top:16px;font-size:14px;font-weight:500}
.status__icons{position:absolute;right:22px;top:18px}
.navbar{top:0;left:0;right:0;height:88px;background:var(--row-bg);box-shadow:0 1px 0 rgba(0,0,0,.03)}
.navbar__row{position:absolute;left:0;right:0;top:56px;height:22px;font-size:17px}
.nav-back{position:absolute;left:10px;color:var(--ios-blue);display:flex;align-items:center;gap:4px}
.nav-title{position:absolute;left:122px;font-weight:400}
.nav-title--center{left:0;right:0;text-align:center}
.nav-action{position:absolute;right:24px;color:var(--ios-blue);font-weight:500}
.nav-menu{position:absolute;left:17px;top:2px}
.forgot__heading{left:24px;top:145px;font-size:20px;font-weight:400}
.forgot__copy{left:24px;top:186px;width:335px;font-size:15.5px;font-weight:300;line-height:21.8px;color:var(--muted)}
.forgot__label{left:24px;top:327px;font-size:13px;color:var(--label)}
.field{left:24px;top:351px;width:324px;height:51px;background:var(--row-bg);border-radius:6px;
  box-shadow:0 2px 8px rgba(0,0,0,.04);display:flex;align-items:center;padding:0 20px;font-size:15.5px;color:#3a3a40}
.field__clear{position:absolute;right:18px;top:19px}
.btn{display:flex;align-items:center;justify-content:center;background:var(--accent);color:#fff;
  border-radius:8px;font-size:16px;font-weight:500;letter-spacing:-.5px}
.btn--reset{position:absolute;left:24px;top:433px;width:324px;height:50px}
.home-indicator{left:120px;bottom:10px;width:133px;height:4px;border-radius:3px;background:var(--black)}
.status-panel{left:25px;top:118px;width:323px;height:90px;background:var(--black);border-radius:8px;
  display:flex;align-items:center;justify-content:center;color:var(--accent);font-size:16.5px;
  letter-spacing:-.3px;box-shadow:0 4px 10px rgba(0,0,0,.18)}
.btn--quick{position:absolute;left:25px;top:235px;width:323px;height:50px;border-radius:7px}
.section-label{left:16px;font-size:12px;color:var(--section-label);letter-spacing:.2px}
.list{left:0;right:0;background:var(--row-bg);border-top:1px solid var(--divider);border-bottom:1px solid var(--divider)}
.row{position:relative;height:54.5px;display:flex;align-items:center;padding-left:16px;font-size:16px}
.row+.row::before{content:"";position:absolute;left:16px;right:0;top:0;border-top:1px solid var(--divider)}
.row__flag{width:32px;height:24px;margin-right:9px}
.row__chev{position:absolute;right:18px;top:21px}
.row__star{position:absolute;right:42px;top:17px}
</style>
</head>
<body>

<section class="screen screen--forgot" aria-label="Forgot password screen">
  <div class="abs navbar"></div>
  <div class="status abs" style="background:transparent">
    <span class="status__time">9:41</span>
    <svg class="status__icons" width="62" height="12" viewBox="0 0 62 12" aria-hidden="true">
      <rect x="0" y="8" width="3" height="4" rx="1"/><rect x="4.5" y="6" width="3" height="6" rx="1"/><rect x="9" y="3.5" width="3" height="8.5" rx="1"/><rect x="13.5" y="1" width="3" height="11" rx="1"/>
      <path d="M21 4.5a9 9 0 0 1 12 0M23.3 7a5.5 5.5 0 0 1 7.4 0M25.6 9.4a2 2 0 0 1 2.8 0" fill="none" stroke="#000" stroke-width="1.6" stroke-linecap="round"/>
      <rect x="38.5" y="1.5" width="20" height="9" rx="2.5" fill="none" stroke="#000" opacity=".4"/><rect x="40" y="3" width="17" height="6" rx="1.5"/><rect x="59.5" y="4.5" width="1.5" height="3" rx=".7" opacity=".4"/>
    </svg>
  </div>
  <div class="abs navbar__row">
    <span class="nav-back">
      <svg width="12" height="20" viewBox="0 0 12 20" aria-hidden="true"><path d="M10 2 2 10l8 8" fill="none" stroke="currentColor" stroke-width="2.4" stroke-linecap="round" stroke-linejoin="round"/></svg>
      Login Page
    </span>
    <span class="nav-title">Forgot Password</span>
  </div>

  <h1 class="abs forgot__heading">Did you forget your Password?</h1>
  <p class="abs forgot__copy">If you have for gotten your password, enter the email address associated with your account into the box below and we will send you instructions on how to reset your password to your email account.</p>
  <span class="abs forgot__label">Email Address:</span>
  <div class="abs field">name@mailbox.test
    <svg class="field__clear" width="13" height="13" viewBox="0 0 13 13" aria-hidden="true"><path d="M1 1l11 11M12 1 1 12" stroke="#9a9aa2" stroke-width="1.4"/></svg>
  </div>
  <div class="btn btn--reset">SUBMIT PASSWORD RESET</div>
  <div class="abs home-indicator"></div>
</section>

<section class="screen screen--home" aria-label="CozyTunnel home screen">
  <div class="abs navbar"></div>
  <div class="status abs" style="background:transparent">
    <span class="status__time">9:41</span>
    <svg class="status__icons" width="62" height="12" viewBox="0 0 62 12" aria-hidden="true">
      <rect x="0" y="8" width="3" height="4" rx="1"/><rect x="4.5" y="6" width="3" height="6" rx="1"/><rect x="9" y="3.5" width="3" height="8.5" rx="1"/><rect x="13.5" y="1" width="3" height="11" rx="1"/>
      <path d="M21 4.5a9 9 0 0 1 12 0M23.3 7a5.5 5.5 0 0 1 7.4 0M25.6 9.4a2 2 0 0 1 2.8 0" fill="none" stroke="#000" stroke-width="1.6" stroke-linecap="round"/>
      <rect x="38.5" y="1.5" width="20" height="9" rx="2.5" fill="none" stroke="#000" opacity=".4"/><rect x="40" y="3" width="17" height="6" rx="1.5"/><rect x="59.5" y="4.5" width="1.5" height="3" rx=".7" opacity=".4"/>
    </svg>
  </div>
  <div class="abs navbar__row">
    <svg class="nav-menu" width="22" height="18" viewBox="0 0 22 18" aria-hidden="true"><path d="M1 1.5h20M1 9h20M1 16.5h20" stroke="var(--ios-blue)" stroke-width="2"/></svg>
    <span class="nav-title nav-title--center">CozyTunnel</span>
    <span class="nav-action">Ping Test&nbsp;&#8942;</span>
  </div>

  <div class="abs status-panel">NOT CONNECTED</div>
  <div class="btn btn--quick">QUICK CONNECT</div>

  <span class="abs section-label" style="top:311px">FAVORITES</span>
  <div class="abs list" style="top:330px">
    <div class="row">
      <svg class="row__flag" role="img" aria-label="United States flag" viewBox="0 0 32 24"><rect width="32" height="20" y="1" fill="#d8323c"/><path d="M0 4h32M0 8h32M0 12h32M0 16h32" stroke="#fff" stroke-width="1.6"/><rect width="14" height="10" y="1" fill="#2b4aa0"/><rect width="1.6" height="24" fill="#222"/></svg>
      USA
      <svg class="row__chev" width="8" height="13" viewBox="0 0 8 13" aria-hidden="true"><path d="M1 1l5.5 5.5L1 12" fill="none" stroke="var(--chevron)" stroke-width="1.6"/></svg>
    </div>
  </div>

  <span class="abs section-label" style="top:408px">SPECIALTY SERVERS</span>
  <div class="abs list" style="top:427px">
    <div class="row">Streaming Servers<svg class="row__chev" width="8" height="13" viewBox="0 0 8 13" aria-hidden="true"><path d="M1 1l5.5 5.5L1 12" fill="none" stroke="var(--chevron)" stroke-width="1.6"/></svg></div>
    <div class="row">P2P Servers<svg class="row__chev" width="8" height="13" viewBox="0 0 8 13" aria-hidden="true"><path d="M1 1l5.5 5.5L1 12" fill="none" stroke="var(--chevron)" stroke-width="1.6"/></svg></div>
    <div class="row">Onion over VPN<svg class="row__chev" width="8" height="13" viewBox="0 0 8 13" aria-hidden="true"><path d="M1 1l5.5 5.5L1 12" fill="none" stroke="var(--chevron)" stroke-width="1.6"/></svg></div>
  </div>

  <span class="abs section-label" style="top:613px">COUNTRY</span>
  <div class="abs list" style="top:633px">
    <div class="row">
      <svg class="row__flag" role="img" aria-label="United States flag" viewBox="0 0 32 24"><rect width="32" height="20" y="1" fill="#d8323c"/><path d="M0 4h32M0 8h32M0 12h32M0 16h32" stroke="#fff" stroke-width="1.6"/><rect width="14" height="10" y="1" fill="#2b4aa0"/><rect width="1.6" height="24" fill="#222"/></svg>
      USA
      <svg class="row__star" width="22" height="21" viewBox="0 0 24 23" aria-hidden="true"><path d="M12 1l3.2 7 7.6.8-5.7 5.1 1.6 7.5L12 17.6 5.3 21.4l1.6-7.5L1.2 8.8l7.6-.8z" fill="var(--star-on)"/></svg>
      <svg class="row__chev" width="8" height="13" viewBox="0 0 8 13" aria-hidden="true"><path d="M1 1l5.5 5.5L1 12" fill="none" stroke="var(--chevron)" stroke-width="1.6"/></svg>
    </div>
    <div class="row">
      <svg class="row__flag" role="img" aria-label="United Kingdom flag" viewBox="0 0 32 24"><rect width="32" height="20" y="1" fill="#24418f"/><path d="M0 1l32 20M32 1 0 21" stroke="#fff" stroke-width="3"/><path d="M16 1v20M0 11h32" stroke="#fff" stroke-width="5"/><path d="M16 1v20M0 11h32" stroke="#d0283a" stroke-width="2.6"/><rect width="1.6" height="24" fill="#222"/></svg>
      UK
      <svg class="row__star" width="22" height="21" viewBox="0 0 24 23" aria-hidden="true"><path d="M12 1l3.2 7 7.6.8-5.7 5.1 1.6 7.5L12 17.6 5.3 21.4l1.6-7.5L1.2 8.8l7.6-.8z" fill="var(--star-off)"/></svg>
      <svg class="row__chev" width="8" height="13" viewBox="0 0 8 13" aria-hidden="true"><path d="M1 1l5.5 5.5L1 12" fill="none" stroke="var(--chevron)" stroke-width="1.6"/></svg>
    </div>
    <div class="row">
      <svg class="row__flag" role="img" aria-label="Canada flag" viewBox="0 0 32 24"><rect width="32" height="20" y="1" fill="#fff"/><rect width="8" height="20" y="1" fill="#d8232f"/><rect x="24" width="8" height="20" y="1" fill="#d8232f"/><circle cx="16" cy="11" r="3.5" fill="#d8232f"/><rect width="1.6" height="24" fill="#222"/></svg>
      Canada
      <svg class="row__star" width="22" height="21" viewBox="0 0 24 23" aria-hidden="true"><path d="M12 1l3.2 7 7.6.8-5.7 5.1 1.6 7.5L12 17.6 5.3 21.4l1.6-7.5L1.2 8.8l7.6-.8z" fill="var(--star-off)"/></svg>
      <svg class="row__chev" width="8" height="13" viewBox="0 0 8 13" aria-hidden="true"><path d="M1 1l5.5 5.5L1 12" fill="none" stroke="var(--chevron)" stroke-width="1.6"/></svg>
    </div>
  </div>
  <div class="abs home-indicator"></div>
</section>

</body>
</html>
```